Podcast website that will AMAZE

I need a Wordpress website designed for my podcast that I am about to launch. The podcast is called 'calm river bright lantern' and is targeted at 30-45 year old professional females. The podcast is aiming to provide listeners with information, from a variety of experts, to improve their health and well-being, but also their financial circumstances. I want a landing page that would appeal to this demographic that is clean and uncluttered. also, I want the ability to play the podcast episodes from the website by integrating with libsyn as the media host. I need the ability to capture their personal information and ability to provide downloadable documents to people who come to the website. Although I would not initially need a shopping cart I will need the ability to add one at a future date. I have attached the current logo to give you an idea of theme

Target Market(s)

30-45 year 0ld professional females with an interest in health

Coding

Coded - Design and coding required

Colors

Designer to choose colors to be used in the design.

Requirements
Must have
• - ability to play podcasts from website. will be using libsyn as media host
• - clean uncluttered layout
• - ability to capture emails from vistors
• - ability to include online store in the future

```html
<!DOCTYPE html>
<html lang="en">
<head>
<meta charset="utf-8">
<title>Calm River Bright Lantern — Podcast</title>
<link rel="stylesheet" href="https://fonts.googleapis.com/css2?family=Poppins:wght@300;400;500;600;700&display=swap">
<style>
:root{
  --purple:#8d3a9d;
  --purple-deep:#6d2f8f;
  --blue:#1f8fdb;
  --blue-light:#29a3e8;
  --ink:#222;
  --muted:#666;
  --rule:#e2e2e2;
  --night:#070707;
  --mist:#f2f2f6;
  --white:#fff;
}
*{box-sizing:border-box;margin:0;padding:0}
html,body{width:1200px;height:2817px;overflow:hidden}
body{font-family:'Poppins',sans-serif;color:var(--ink);background:var(--white);position:relative}
.wrap{position:absolute;left:160px;width:880px}

/* header */
.site-header{position:absolute;top:0;left:0;width:1200px;height:88px;background:var(--night)}
.brand{position:absolute;left:160px;top:16px;display:flex;align-items:center;gap:10px}
.brand-dot{width:40px;height:40px;border-radius:50%;border:2px solid var(--blue)}
.brand-name{color:var(--purple);font-weight:600;font-size:15px;line-height:17px;text-transform:uppercase;width:150px}
.main-nav{position:absolute;left:428px;top:35px;display:flex;gap:38px;font-size:11px;font-weight:500;color:var(--white)}
.main-nav .active{color:var(--blue-light)}
.header-tools{position:absolute;left:946px;top:22px;display:flex;gap:8px}
.tool{width:42px;height:42px;border-radius:50%;border:2px solid var(--purple);display:flex;align-items:center;justify-content:center}
.tool.search{border-color:var(--blue)}

/* hero */
.hero{position:absolute;top:88px;left:0;width:1200px;height:534px;background:linear-gradient(90deg,#9a3f9a 0%,#6a4ab0 35%,#3d6fc6 65%,#1d8fe0 100%)}
.hero-photo{position:absolute;inset:0;background:radial-gradient(ellipse 260px 320px at 540px 250px,rgba(230,200,220,.35),transparent 70%),radial-gradient(ellipse 300px 200px at 120px 380px,rgba(120,60,120,.45),transparent 70%)}
.hero-kicker{position:absolute;left:162px;top:142px;color:var(--white);font-size:14px}
.hero-title{position:absolute;left:162px;top:176px;color:var(--white);font-size:22px;font-weight:600;line-height:34px;width:440px;text-transform:uppercase}
.hero-meta{position:absolute;left:164px;top:262px;display:flex;gap:22px;color:var(--white);font-size:11px;align-items:center}
.hero-meta span{display:flex;align-items:center;gap:5px}
.hero-arrow{position:absolute;top:238px;color:var(--white);font-size:22px;font-weight:300}
.player{position:absolute;left:0;top:468px;width:1200px;height:66px;background:rgba(10,10,30,.45);display:flex;align-items:center}
.player-controls{position:absolute;left:250px;top:18px;display:flex;align-items:center;gap:2px}
.pc{border:1.5px solid var(--white);border-radius:50%;display:flex;align-items:center;justify-content:center}
.player-time{position:absolute;left:754px;top:26px;color:var(--white);font-size:10px}
.player-volume{position:absolute;left:858px;top:24px;display:flex;align-items:center;gap:10px}

/* podcasts */
.section-title{font-size:20px;font-weight:700;text-transform:uppercase}
.section-title .a{color:var(--purple)}
.section-title .b{color:var(--blue)}
.podcasts-title{top:664px}
.podcast-grid{top:725px;display:grid;grid-template-columns:repeat(3,280px);column-gap:20px;row-gap:22px}
.episode{border:1px solid var(--rule);height:375px;position:relative;background:var(--white)}
.episode-photo{height:178px;position:relative}
.episode-stats{position:absolute;right:10px;top:14px;color:var(--white);font-size:9px;display:flex;gap:8px}
.episode-body{padding:12px 13px 0}
.episode-title{color:var(--purple);font-size:15px;font-weight:500;margin-bottom:10px}
.episode-text{font-size:10.5px;line-height:22px;color:#333}
.episode-meta{font-size:10px;color:var(--muted);margin-top:10px;display:flex;gap:14px}
.episode-foot{position:absolute;left:0;right:0;bottom:0;height:60px;border-top:1px solid var(--rule);display:flex;align-items:center;justify-content:space-between;padding:0 16px 0 13px}
.listen{background:linear-gradient(90deg,var(--purple-deep),var(--blue));color:var(--white);font-size:10px;font-weight:600;border-radius:15px;padding:7px 18px;text-transform:uppercase}
.ph1{background:linear-gradient(135deg,#7ab35a,#c9b49e)}
.ph2{background:linear-gradient(135deg,#c97a7f,#8b86a0)}
.ph3{background:linear-gradient(135deg,#5d8a3a,#a7b98a)}
.ph4{background:linear-gradient(135deg,#d9a5a8,#b44a70)}
.ph5{background:linear-gradient(135deg,#c69a2a,#5a6b2c)}
.ph6{background:linear-gradient(135deg,#6f8d5a,#d8c9d6)}

/* store */
.store{position:absolute;top:1572px;left:0;width:1200px;height:469px;background:var(--mist);border-top:2px solid var(--blue)}
.store-tab{position:absolute;left:454px;top:-2px;width:300px;height:48px;background:linear-gradient(90deg,var(--purple),var(--blue));clip-path:polygon(0 0,100% 0,88% 100%,12% 100%);color:var(--white);font-size:18px;font-weight:600;text-align:center;line-height:46px}
.store-grid{position:absolute;left:163px;top:88px;display:grid;grid-template-columns:repeat(4,212px);column-gap:10px}
.product{background:var(--white);border:1px solid var(--rule);height:295px;padding:6px;text-align:center}
.product-photo{height:150px;border:1px solid var(--rule)}
.price{color:var(--blue);font-size:20px;font-weight:500;margin-top:16px}
.product-name{font-size:11px;font-weight:500;text-transform:uppercase;margin-top:8px}
.product-actions{display:flex;justify-content:center;gap:8px;margin-top:16px}
.pa{width:28px;height:28px;border-radius:50%;border:1px solid #999;display:flex;align-items:center;justify-content:center}
.product.featured .pa{border-color:var(--purple)}

/* about */
.about-title{top:2090px}
.about-text{top:2138px;width:430px;font-size:10.5px;line-height:24px;color:#333}
.about-ring{position:absolute;left:748px;top:2076px;width:290px;height:290px;border-radius:50%;border:14px solid #ececec}
.about-portrait{position:absolute;left:806px;top:2092px;width:220px;height:296px;border-radius:110px 110px 0 0;background:linear-gradient(180deg,#e9c98e 0%,#d9a88a 40%,#b8323a 75%,#8e2430 100%)}

/* signup */
.signup{position:absolute;top:2325px;left:0;width:1200px;height:173px;background:linear-gradient(90deg,var(--purple) 0%,#6a54b8 50%,var(--blue) 100%);clip-path:polygon(0 0,700px 0,760px 55px,1200px 55px,1200px 100%,0 100%)}
.signup-title{position:absolute;left:160px;top:27px;color:var(--white);font-size:24px;font-weight:600;text-transform:uppercase}
.signup-sub{position:absolute;left:160px;top:62px;color:var(--white);font-size:13px}
.signup-form{position:absolute;left:162px;top:95px;display:flex;gap:6px}
.field{width:384px;height:38px;background:var(--white);font-size:12px;color:#333;padding:11px 10px}
.signup-btn{width:98px;height:38px;background:var(--purple);color:var(--white);font-size:12px;font-weight:600;text-align:center;line-height:38px}

/* footer */
.site-footer{position:absolute;top:2498px;left:0;width:1200px;height:319px;background:var(--night);color:var(--white)}
.footer-brand{position:absolute;left:170px;top:50px;display:flex;align-items:center;gap:10px}
.footer-about{position:absolute;left:160px;top:136px;width:260px;font-size:10.5px;line-height:24px}
.footer-col{position:absolute;top:42px}
.footer-col h4{font-size:16px;font-weight:400;margin-bottom:18px}
.footer-col li{list-style:none;font-size:10.5px;line-height:24px}
.contact li{display:flex;gap:10px;align-items:flex-start}
.contact svg{flex:none;margin-top:7px}
.footer-bottom{position:absolute;left:160px;top:265px;width:880px;border-top:1px solid #1e1e1e;padding-top:10px;font-size:10.5px}
.socials{position:absolute;left:902px;top:253px;display:flex;gap:8px}
.social{width:28px;height:28px;border-radius:50%;background:#4a6fd0}
</style>
</head>
<body>

<header class="site-header">
  <div class="brand"><span class="brand-dot"></span><span class="brand-name">Calm River Bright Lantern</span></div>
  <nav class="main-nav"><span class="active">HOME</span><span>ABOUT US</span><span>PRODUCTS</span><span>PODCASTS</span><span>BLOG</span><span>CONTACT</span></nav>
  <div class="header-tools">
    <span class="tool"><svg width="14" height="14" viewBox="0 0 24 24" fill="#c23a9a"><path d="M2 3h3l3 12h11l3-9H7" stroke="#c23a9a" stroke-width="2" fill="none"/><circle cx="9" cy="20" r="2"/><circle cx="18" cy="20" r="2"/></svg></span>
    <span class="tool search"><svg width="14" height="14" viewBox="0 0 24 24" fill="none" stroke="#9bd41e" stroke-width="3"><circle cx="10" cy="10" r="6"/><path d="M15 15l6 6"/></svg></span>
  </div>
</header>

<section class="hero">
  <div class="hero-photo" role="img" aria-label="Woman with arms spread outdoors, eyes closed, under a purple-to-blue colour wash"></div>
  <span class="hero-arrow" style="left:42px">‹</span>
  <span class="hero-arrow" style="left:1130px">›</span>
  <p class="hero-kicker">Calm River Bright Lantern #2</p>
  <h1 class="hero-title">Sed ut perspiciatis unde omnisste natus error sit voem accur.</h1>
  <div class="hero-meta">
    <span>APR 23, 2018</span>
    <span><svg width="10" height="10" viewBox="0 0 10 10" fill="none" stroke="#fff"><circle cx="5" cy="5" r="4"/><path d="M5 3v2h2"/></svg>36 min</span>
    <span>38 <svg width="10" height="9" viewBox="0 0 10 9" fill="#fff"><path d="M5 9L1 5a2.3 2.3 0 0 1 4-3 2.3 2.3 0 0 1 4 3z"/></svg></span>
    <span>23 <svg width="10" height="9" viewBox="0 0 10 9" fill="#fff"><path d="M1 1h8v5H4L2 8V6H1z"/></svg></span>
  </div>
  <div class="player">
    <div class="player-controls">
      <span class="pc" style="width:18px;height:18px"><svg width="8" height="8" viewBox="0 0 8 8" fill="#fff"><path d="M6 1v6L2 4z"/></svg></span>
      <span class="pc" style="width:30px;height:30px;border-width:2px"><svg width="10" height="12" viewBox="0 0 10 12" fill="#fff"><rect x="1" y="1" width="3" height="10"/><rect x="6" y="1" width="3" height="10"/></svg></span>
      <span class="pc" style="width:18px;height:18px"><svg width="8" height="8" viewBox="0 0 8 8" fill="#fff"><path d="M2 1v6l4-3z"/></svg></span>
    </div>
    <svg style="position:absolute;left:360px;top:12px" width="376" height="42" viewBox="0 0 376 42">
      <g fill="#fff" opacity=".9">
        <rect x="0" y="18" width="2" height="6"/><rect x="6" y="14" width="2" height="14"/><rect x="12" y="10" width="2" height="22"/><rect x="18" y="16" width="2" height="10"/><rect x="24" y="8" width="2" height="26"/><rect x="30" y="13" width="2" height="16"/><rect x="36" y="6" width="2" height="30"/><rect x="42" y="12" width="2" height="18"/><rect x="48" y="9" width="2" height="24"/><rect x="54" y="15" width="2" height="12"/><rect x="60" y="4" width="2" height="34"/><rect x="66" y="11" width="2" height="20"/><rect x="72" y="14" width="2" height="14"/><rect x="78" y="7" width="2" height="28"/><rect x="84" y="12" width="2" height="18"/><rect x="90" y="16" width="2" height="10"/><rect x="96" y="9" width="2" height="24"/><rect x="102" y="13" width="2" height="16"/><rect x="108" y="5" width="2" height="32"/><rect x="114" y="12" width="2" height="18"/>
      </g>
      <g fill="#fff" opacity=".55">
        <rect x="120" y="10" width="2" height="22"/><rect x="126" y="14" width="2" height="14"/><rect x="132" y="6" width="2" height="30"/><rect x="138" y="12" width="2" height="18"/><rect x="144" y="16" width="2" height="10"/><rect x="150" y="8" width="2" height="26"/><rect x="156" y="13" width="2" height="16"/><rect x="162" y="10" width="2" height="22"/><rect x="168" y="5" width="2" height="32"/><rect x="174" y="14" width="2" height="14"/><rect x="180" y="9" width="2" height="24"/><rect x="186" y="12" width="2" height="18"/><rect x="192" y="7" width="2" height="28"/><rect x="198" y="15" width="2" height="12"/><rect x="204" y="10" width="2" height="22"/><rect x="210" y="13" width="2" height="16"/><rect x="216" y="6" width="2" height="30"/><rect x="222" y="11" width="2" height="20"/><rect x="228" y="16" width="2" height="10"/><rect x="234" y="8" width="2" height="26"/><rect x="240" y="12" width="2" height="18"/><rect x="246" y="9" width="2" height="24"/><rect x="252" y="14" width="2" height="14"/><rect x="258" y="7" width="2" height="28"/><rect x="264" y="12" width="2" height="18"/><rect x="270" y="15" width="2" height="12"/><rect x="276" y="9" width="2" height="24"/><rect x="282" y="13" width="2" height="16"/><rect x="288" y="6" width="2" height="30"/><rect x="294" y="12" width="2" height="18"/><rect x="300" y="10" width="2" height="22"/><rect x="306" y="15" width="2" height="12"/><rect x="312" y="8" width="2" height="26"/><rect x="318" y="13" width="2" height="16"/><rect x="324" y="11" width="2" height="20"/><rect x="330" y="16" width="2" height="10"/><rect x="336" y="9" width="2" height="24"/><rect x="342" y="14" width="2" height="14"/><rect x="348" y="12" width="2" height="18"/><rect x="354" y="16" width="2" height="10"/><rect x="360" y="13" width="2" height="16"/><rect x="366" y="17" width="2" height="8"/><rect x="372" y="19" width="2" height="4"/>
      </g>
      <circle cx="117" cy="21" r="4" fill="#fff"/>
    </svg>
    <span class="player-time">24:45 | 36:12</span>
    <div class="player-volume">
      <span class="pc" style="width:18px;height:18px"><svg width="8" height="8" viewBox="0 0 8 8" fill="#fff"><path d="M1 3h2l2-2v6L3 5H1z"/></svg></span>
      <svg width="80" height="8" viewBox="0 0 80 8"><path d="M0 4h80" stroke="#fff" stroke-width="1.5"/><circle cx="52" cy="4" r="4" fill="#fff"/></svg>
    </div>
  </div>
</section>

<h2 class="wrap section-title podcasts-title" style="padding-left:2px"><span class="a">Latest</span> <span class="b">Podcasts</span></h2>

<div class="wrap podcast-grid">
  <article class="episode"><div class="episode-photo ph1" role="img" aria-label="Portrait of a smiling woman in glasses outdoors"><span class="episode-stats">12 ♥ 8 ●</span></div><div class="episode-body"><h3 class="episode-title">Sed ut persiatis uemn istenatu</h3><p class="episode-text">Sed ut perspiciatis unde omnis istusrror sit voluptatem accud ut perspici lore.</p><p class="episode-meta"><span>Apr 19, 2018</span><span>◷ 54 min</span></p></div><div class="episode-foot"><span class="listen">Listen now →</span><svg width="14" height="14" viewBox="0 0 14 14" fill="none" stroke="#aaa"><rect x="1" y="1" width="12" height="12"/><path d="M7 3v6M4 6l3 3 3-3"/></svg></div></article>
  <article class="episode"><div class="episode-photo ph2" role="img" aria-label="Woman with arms crossed against a pink wall"><span class="episode-stats">12 ♥ 8 ●</span></div><div class="episode-body"><h3 class="episode-title">Sed ut persiatis uemn istenatu</h3><p class="episode-text">Sed ut perspiciatis unde omnis istusrror sit voluptatem accud ut perspici lore.</p><p class="episode-meta"><span>Apr 19, 2018</span><span>◷ 54 min</span></p></div><div class="episode-foot"><span class="listen">Listen now →</span><svg width="14" height="14" viewBox="0 0 14 14" fill="none" stroke="#aaa"><rect x="1" y="1" width="12" height="12"/><path d="M7 3v6M4 6l3 3 3-3"/></svg></div></article>
  <article class="episode"><div class="episode-photo ph3" role="img" aria-label="Woman in a tweed jacket among green foliage"><span class="episode-stats">12 ♥ 8 ●</span></div><div class="episode-body"><h3 class="episode-title">Sed ut persiatis uemn istenatu</h3><p class="episode-text">Sed ut perspiciatis unde omnis istusrror sit voluptatem accud ut perspici lore.</p><p class="episode-meta"><span>Apr 19, 2018</span><span>◷ 54 min</span></p></div><div class="episode-foot"><span class="listen">Listen now →</span><svg width="14" height="14" viewBox="0 0 14 14" fill="none" stroke="#aaa"><rect x="1" y="1" width="12" height="12"/><path d="M7 3v6M4 6l3 3 3-3"/></svg></div></article>
  <article class="episode"><div class="episode-photo ph4" role="img" aria-label="Woman in a pink scarf smiling indoors"><span class="episode-stats">12 ♥ 8 ●</span></div><div class="episode-body"><h3 class="episode-title">Sed ut persiatis uemn istenatu</h3><p class="episode-text">Sed ut perspiciatis unde omnis istusrror sit voluptatem accud ut perspici lore.</p><p class="episode-meta"><span>Apr 19, 2018</span><span>◷ 54 min</span></p></div><div class="episode-foot"><span class="listen">Listen now →</span><svg width="14" height="14" viewBox="0 0 14 14" fill="none" stroke="#aaa"><rect x="1" y="1" width="12" height="12"/><path d="M7 3v6M4 6l3 3 3-3"/></svg></div></article>
  <article class="episode"><div class="episode-photo ph5" role="img" aria-label="Woman sitting beside a bicycle in an autumn park"><span class="episode-stats">12 ♥ 8 ●</span></div><div class="episode-body"><h3 class="episode-title">Sed ut persiatis uemn istenatu</h3><p class="episode-text">Sed ut perspiciatis unde omnis istusrror sit voluptatem accud ut perspici lore.</p><p class="episode-meta"><span>Apr 19, 2018</span><span>◷ 54 min</span></p></div><div class="episode-foot"><span class="listen">Listen now →</span><svg width="14" height="14" viewBox="0 0 14 14" fill="none" stroke="#aaa"><rect x="1" y="1" width="12" height="12"/><path d="M7 3v6M4 6l3 3 3-3"/></svg></div></article>
  <article class="episode"><div class="episode-photo ph6" role="img" aria-label="Woman among flowering plants at a garden market"><span class="episode-stats">12 ♥ 8 ●</span></div><div class="episode-body"><h3 class="episode-title">Sed ut persiatis uemn istenatu</h3><p class="episode-text">Sed ut perspiciatis unde omnis istusrror sit voluptatem accud ut perspici lore.</p><p class="episode-meta"><span>Apr 19, 2018</span><span>◷ 54 min</span></p></div><div class="episode-foot"><span class="listen">Listen now →</span><svg width="14" height="14" viewBox="0 0 14 14" fill="none" stroke="#aaa"><rect x="1" y="1" width="12" height="12"/><path d="M7 3v6M4 6l3 3 3-3"/></svg></div></article>
</div>

<section class="store">
  <div class="store-tab">ONLINE STORE</div>
  <div class="store-grid">
    <div class="product featured"><div class="product-photo" role="img" aria-label="Protein tub and dumbbell" style="background:radial-gradient(circle at 50% 55%,#5c6f8c 0 28%,#eef0f4 30%)"></div><p class="price">$ 59.00</p><p class="product-name">Finibus Bonorum</p><div class="product-actions"><span class="pa"><svg width="11" height="11" viewBox="0 0 24 24" fill="none" stroke="#8d3a9d" stroke-width="2.5"><path d="M2 3h3l3 12h11l3-9H7"/></svg></span><span class="pa"><svg width="11" height="11" viewBox="0 0 10 9" fill="none" stroke="#8d3a9d"><path d="M5 8.5L1 5a2.3 2.3 0 0 1 4-3 2.3 2.3 0 0 1 4 3z"/></svg></span><span class="pa"><svg width="11" height="11" viewBox="0 0 12 12" fill="none" stroke="#8d3a9d" stroke-width="1.4"><path d="M1 4h10M8 1l3 3M11 8H1M4 11L1 8"/></svg></span></div></div>
    <div class="product"><div class="product-photo" role="img" aria-label="Protein tubs with pink dumbbells" style="background:radial-gradient(circle at 50% 55%,#c8345f 0 26%,#eef0f4 28%)"></div><p class="price">$ 99.00</p><p class="product-name">Finibus Bono Lirenrum</p><div class="product-actions"><span class="pa"><svg width="11" height="11" viewBox="0 0 24 24" fill="none" stroke="#888" stroke-width="2.5"><path d="M2 3h3l3 12h11l3-9H7"/></svg></span><span class="pa"><svg width="11" height="11" viewBox="0 0 10 9" fill="none" stroke="#888"><path d="M5 8.5L1 5a2.3 2.3 0 0 1 4-3 2.3 2.3 0 0 1 4 3z"/></svg></span><span class="pa"><svg width="11" height="11" viewBox="0 0 12 12" fill="none" stroke="#888" stroke-width="1.4"><path d="M1 4h10M8 1l3 3M11 8H1M4 11L1 8"/></svg></span></div></div>
    <div class="product"><div class="product-photo" role="img" aria-label="Plain black supplement jar" style="background:radial-gradient(ellipse 30px 48px at 50% 55%,#111 0 95%,#f3f3f5 100%)"></div><p class="price">$ 79.00</p><p class="product-name">Finibus Bono Lirenrum</p><div class="product-actions"><span class="pa"><svg width="11" height="11" viewBox="0 0 24 24" fill="none" stroke="#888" stroke-width="2.5"><path d="M2 3h3l3 12h11l3-9H7"/></svg></span><span class="pa"><svg width="11" height="11" viewBox="0 0 10 9" fill="none" stroke="#888"><path d="M5 8.5L1 5a2.3 2.3 0 0 1 4-3 2.3 2.3 0 0 1 4 3z"/></svg></span><span class="pa"><svg width="11" height="11" viewBox="0 0 12 12" fill="none" stroke="#888" stroke-width="1.4"><path d="M1 4h10M8 1l3 3M11 8H1M4 11L1 8"/></svg></span></div></div>
    <div class="product"><div class="product-photo" role="img" aria-label="Supplement tubs with a shaker bottle" style="background:radial-gradient(circle at 50% 55%,#2d4a78 0 28%,#eef0f4 30%)"></div><p class="price">$ 69.00</p><p class="product-name">Finibus Bono Lirenrum</p><div class="product-actions"><span class="pa"><svg width="11" height="11" viewBox="0 0 24 24" fill="none" stroke="#888" stroke-width="2.5"><path d="M2 3h3l3 12h11l3-9H7"/></svg></span><span class="pa"><svg width="11" height="11" viewBox="0 0 10 9" fill="none" stroke="#888"><path d="M5 8.5L1 5a2.3 2.3 0 0 1 4-3 2.3 2.3 0 0 1 4 3z"/></svg></span><span class="pa"><svg width="11" height="11" viewBox="0 0 12 12" fill="none" stroke="#888" stroke-width="1.4"><path d="M1 4h10M8 1l3 3M11 8H1M4 11L1 8"/></svg></span></div></div>
  </div>
</section>

<h2 class="wrap section-title about-title" style="padding-left:4px"><span class="a">About</span> <span class="b">Calm River Bright Lantern</span></h2>
<p class="wrap about-text">Sed ut perspiciatis unde omnis iste natus error sit voluptatem accusantium dol oremque laudantium, totam rem aperiam, eaque ipsa quae ab illo inventore ver itatis et quasi architecto beatae vitae dicta sunt explicabo. Nemo enim ipsam v oluptatem quia voluptas sit sed quia consequuntur magni dolores eos qui ratio ne voluptatem sequi nesciueatae vitae dicta sunt explicabo. Nemo enim ipsam voluptatem quia voluptas sit sed quia co.</p>
<div class="about-ring"></div>
<div class="about-portrait" role="img" aria-label="Portrait of the smiling host in a red plaid shirt"></div>

<section class="signup">
  <h2 class="signup-title">Podcasts Signup</h2>
  <p class="signup-sub">Lorem ipsum dolor sit amet, consectetur adipiscing elit, sedeiu.</p>
  <div class="signup-form"><span class="field">Name:</span><span class="field">Email:</span><span class="signup-btn">SIGNUP</span></div>
</section>

<footer class="site-footer">
  <div class="footer-brand"><span class="brand-dot"></span><span class="brand-name">Calm River Bright Lantern</span></div>
  <p class="footer-about">Sed ut perspiciatis unde omnis istusrror sit voluptatem accud ut perspici lored ut pers piciatis unde omnis istusrror sit vol.</p>
  <div class="footer-col" style="left:450px"><h4>Information</h4><ul><li>Sed ut perspiciatis</li><li>Unde omnis iste natus</li><li>Voluptatem accusan</li><li>Tium doloremque</li><li>Haudantium</li></ul></div>
  <div class="footer-col" style="left:666px"><h4>Links</h4><ul><li>Sed ut perspiciatis</li><li>Unde omnis iste natus</li><li>Voluptatem accusan</li><li>Tium doloremque</li><li>Haudantium</li></ul></div>
  <div class="footer-col contact" style="left:873px"><h4>Contact</h4><ul>
    <li><svg width="8" height="10" viewBox="0 0 8 10" fill="#4a6fd0"><path d="M4 0a4 4 0 0 1 4 4c0 3-4 6-4 6S0 7 0 4a4 4 0 0 1 4-4z"/></svg><span>4820 Maple Fern Way, Suite 12,<br>Willow Bay, CA 90000</span></li>
    <li><svg width="9" height="9" viewBox="0 0 10 10" fill="#4a6fd0"><path d="M2 0l2 2-1 2 3 3 2-1 2 2-2 2C4 10 0 6 0 2z"/></svg><span>Tel: (555) 201-3478</span></li>
    <li><svg width="9" height="9" viewBox="0 0 10 10" fill="#4a6fd0"><rect y="3" width="10" height="6"/><rect x="2" y="0" width="6" height="3"/></svg><span>Fax: (555) 201-3479</span></li>
    <li><svg width="10" height="8" viewBox="0 0 10 8" fill="#4a6fd0"><rect width="10" height="8"/></svg><span>hello@calmriverlantern.example</span></li>
  </ul></div>
  <p class="footer-bottom">© 2018 Calm river bright lantern.All rights are reserved. Privacy | Terms of use</p>
  <div class="socials"><span class="social"></span><span class="social"></span><span class="social"></span><span class="social"></span></div>
</footer>

</body>
</html>
```